Business card design needed

I need a business card for my new Food & Lifestyle Coaching business - "Bloomvale Food & Lifestlye Coaching"

i already have a logo and would like to have that incorporated into the business card, obviously.

i would like a design that says "fresh" and "funky" - my target market is female, aged 20-45 so i want something that will stand out to them when they see it.

My "Company Colour" is Apple Green
Updates

Thankyou to everyone who has submitted a design for my project. At this stage i have quite a large number of designs to chose from and with only a short time until my project closes i am focusing now on chosing from those i have already shortlisted so am unfortunately not considering any new desings.

Thankyou again for your interest in my project.

Target Market(s)

Female, Health Conscious (or looking to improve their health/lifestyle), aged between 20-45

Industry/Entity Type

Business

Contact Information for Business Card

Tamsin Corley
Ph: 0417382946
Email: eatwell@marovex.com

Requirements
Must have
• Must include my existing Logo
Nice to have
• Would be nice to incoirporate and appointment card on the back

```html
<!DOCTYPE html>
<html lang="en">
<head>
<meta charset="utf-8">
<title>Bloomvale Food &amp; Lifestyle Coaching – Business Card</title>
<link rel="stylesheet" href="https://fonts.googleapis.com/css2?family=Questrial&display=swap">
<style>
  :root {
    --apple-green: #8cc63f;
    --apple-green-deep: #7ab52f;
    --ink: #1c1c1c;
    --paper: #ffffff;
    --backdrop: #ece9e4;
    --card-shadow: 0 4px 10px rgba(0, 0, 0, 0.28);
  }
  * { box-sizing: border-box; margin: 0; padding: 0; }
  html, body {
    width: 1200px;
    height: 1200px;
    overflow: hidden;
  }
  body {
    background: var(--backdrop);
    font-family: "Questrial", "Century Gothic", sans-serif;
    position: relative;
  }
  .card {
    position: absolute;
    width: 852px;
    height: 521px;
    box-shadow: var(--card-shadow);
    overflow: hidden;
  }

  /* Front */
  .card--front {
    left: 31px;
    top: 31px;
    background: var(--paper);
  }
  .brand {
    position: absolute;
    left: 95px;
    top: 62px;
    display: flex;
    align-items: center;
    gap: 28px;
  }
  .brand__dot {
    width: 130px;
    height: 130px;
    border-radius: 50%;
    background: var(--apple-green);
    flex: none;
  }
  .brand__name {
    font-size: 108px;
    line-height: 1;
    color: var(--ink);
    letter-spacing: -1px;
  }
  .brand__tagline {
    position: absolute;
    left: 370px;
    top: 270px;
    font-size: 27px;
    color: var(--ink);
  }
  .brand__rule {
    position: absolute;
    left: 230px;
    top: 312px;
    width: 600px;
    height: 4px;
  }
  .contact-band {
    position: absolute;
    left: 0;
    bottom: 0;
    width: 100%;
    height: 132px;
    background: var(--apple-green);
    color: var(--paper);
    text-align: right;
    padding: 14px 12px 0 0;
  }
  .contact-band__name {
    font-size: 52px;
    line-height: 1.05;
    text-transform: uppercase;
    letter-spacing: 0.5px;
  }
  .contact-band__sep {
    display: inline-block;
    width: 12px;
    height: 12px;
    border-radius: 50%;
    background: var(--paper);
    margin: 0 16px;
    vertical-align: middle;
  }
  .contact-band__details {
    font-size: 28px;
    margin-top: 6px;
    letter-spacing: 0.3px;
  }

  /* Back */
  .card--back {
    left: 329px;
    top: 622px;
    width: 854px;
    height: 523px;
    background: var(--apple-green);
    color: var(--ink);
  }
  .appointment__title {
    position: absolute;
    left: 26px;
    top: 222px;
    font-size: 54px;
    font-weight: 400;
    letter-spacing: 0.5px;
  }
  .appointment__field {
    position: absolute;
    left: 26px;
    display: flex;
    align-items: baseline;
    font-size: 30px;
  }
  .appointment__field--date { top: 350px; }
  .appointment__field--time { top: 468px; }
  .appointment__line {
    display: inline-block;
    margin-left: 4px;
    border-bottom: 3px dotted var(--ink);
    height: 1px;
    opacity: 0.75;
  }
  .appointment__field--date .appointment__line { width: 630px; }
  .appointment__field--time .appointment__line { width: 638px; }
</style>
</head>
<body>

<section class="card card--front" aria-label="Business card front">
  <div class="brand">
    <span class="brand__dot" aria-hidden="true"></span>
    <span class="brand__name">Bloomvale</span>
  </div>
  <p class="brand__tagline">Food &amp; Lifestyle Coaching</p>
  <svg class="brand__rule" viewBox="0 0 600 4" aria-hidden="true">
    <line x1="0" y1="2" x2="600" y2="2" stroke="var(--apple-green)" stroke-width="2" stroke-dasharray="2 4"/>
  </svg>
  <div class="contact-band">
    <p class="contact-band__name">Tamsin<span class="contact-band__sep" aria-hidden="true"></span>Corley</p>
    <p class="contact-band__details">Ph: 0417382946 Email: eatwell@marovex.com</p>
  </div>
</section>

<section class="card card--back" aria-label="Appointment card back">
  <h2 class="appointment__title">OUR NEXT APPOINTMENT</h2>
  <p class="appointment__field appointment__field--date">Date:<span class="appointment__line"></span></p>
  <p class="appointment__field appointment__field--time">Time:<span class="appointment__line"></span></p>
</section>

</body>
</html>
```